wolterhagen.info (Physiotherapeut)   //   quellbrand-athletic Webseite
wolterhagen.info (Physiotherapeut) // quellbrand-athletic Webseite
Zielgruppe
Die angesprochene Zielgruppe ist sportlich unterwegs (Sportler jeglicher Sportrichtung). Der externe Shop geht in Richtung Apparels / Kleidung.
Vielleicht wird es aber auch nur eine Physio-Seite und die Apparels kommen im zweiten Schritt - das liegt am Design das man mir präsentiert .... Also legt los ...
(KELVARO wird HOST)
Aufgabenstellung
Mein Name ist Jonathan Wolterhagen ich bin Physiotherapeut / Osteopath (etc).
Die Domain www.wolterhagen.info gehört mir und es würde auch für den Anfang reichen eine digitale Visitenkarte von mir zu erstellen ...
Weiter möchte ich eine Webseite mit dem Namen "quellbrand-athletic" eröffnen. [COM/DE]
Die zu kreierenden Seiten innerhalb der Domain quellbrand-athleti sind:
Main-/LandingPage,
ShopPage (Weiterleitung zu einer externen Webseite),
Impressum,
KooperationsPage (andere Projekte bzw. Webseiten von mir, die in Zukunft kommen).
Design-Vorschläge und umsetzbare / hochladbare Pages (KELVARO) oder NUR Grafiken sind gerne gesehen ...
Die angesprochene Zielgruppe ist sportlich unterwegs (Sportler jeglicher Sportrichtung). Der externe Shop geht in Richtung Apparels.
Die angesprochenen Kreaturen brauchen ein Heim, dass durch ein Schloss repräsentiert werden soll. Evtl. ein Labor. Nicht zu kindlich! Nicht zu düster oder blutig.
Was ich möchte ist: Corporate Identity, eine Webpage (host der Domain wird KELVARO), Logo, etc
Zweiter Schritt wird sein: Grafiken für die Apparels / Klamotten.

```html
<!DOCTYPE html>
<html lang="de">
<head>
<meta charset="utf-8">
<title>wolterhagen – Physiotherapeut</title>
<link href="https://fonts.googleapis.com/css2?family=Cabin:wght@400;600&family=Josefin+Sans:wght@300;400&display=swap" rel="stylesheet">
<style>
  :root {
    --green: #3dbf46;
    --green-dark: #2fa63a;
    --green-deep: #279a33;
    --green-text: #4bae3c;
    --hero-bg: #efeee8;
    --ink: #6f6f6f;
    --ink-dark: #2b2b2b;
    --line: #d8d8d2;
    --white: #ffffff;
  }
  * { margin: 0; padding: 0; box-sizing: border-box; }
  html, body { width: 1086px; height: 1200px; overflow: hidden; background: var(--white); }
  body { position: relative; font-family: "Cabin", Arial, sans-serif; color: var(--ink); }

  .hero { position: absolute; left: 0; top: 0; width: 1086px; height: 446px; background: var(--hero-bg); overflow: hidden; }
  .hero-photo { position: absolute; left: 500px; top: 0; width: 586px; height: 446px;
    background: linear-gradient(90deg, rgba(239,238,232,1) 0%, rgba(170,185,150,0.6) 30%, #8aa07a 55%, #7a5a44 80%, #9a4a30 100%); }
  .hero-photo::after { content: ""; position: absolute; inset: 0;
    background: linear-gradient(180deg, rgba(255,255,255,0) 40%, rgba(239,238,232,0.35) 100%); }

  .brand { position: absolute; left: 189px; top: 20px; }
  .brand-name { font-weight: 600; font-size: 19px; color: var(--green-text); line-height: 1; }
  .brand-tag { font-size: 5px; letter-spacing: 3.4px; color: var(--green-text); margin-top: 3px; }

  .nav { position: absolute; top: 33px; left: 0; font-size: 8px; font-weight: 600; letter-spacing: 0.2px; }
  .nav a { position: absolute; white-space: nowrap; color: #8a8a80; text-decoration: none; }
  .nav .active { color: var(--ink-dark); }
  .nav-marker { position: absolute; left: 489px; top: 0; width: 67px; height: 3px; background: var(--green); }
  .social { position: absolute; top: 26px; width: 22px; height: 22px; border-radius: 50%; }
  .social.one { left: 839px; background: #4a6aa8; }
  .social.two { left: 874px; background: #1fb6e6; }

  .hero-divider { position: absolute; top: 168px; height: 1px; background: var(--line); }
  .hero-dot { position: absolute; left: 536px; top: 162px; width: 13px; height: 13px; border-radius: 50%; background: #2f4a32; }
  .hero-title { position: absolute; left: 0; width: 1086px; top: 210px; text-align: center;
    font-family: "Josefin Sans", Arial, sans-serif; font-weight: 300; font-size: 26px; letter-spacing: 1.8px; color: var(--green-text); }
  .hero-copy { position: absolute; left: 353px; width: 380px; text-align: center; font-family: "Josefin Sans", Arial, sans-serif;
    font-weight: 300; font-size: 9.5px; line-height: 11.5px; color: var(--ink); }

  .contact-band { position: absolute; left: 0; top: 446px; width: 1086px; height: 148px;
    background: linear-gradient(90deg, #3a9e45 0%, var(--green) 25%, var(--green) 70%, #57c35a 100%); }
  .band-photo { position: absolute; left: 0; top: 0; width: 260px; height: 148px;
    background: linear-gradient(90deg, rgba(40,120,50,0.55), rgba(61,191,70,0)); }
  .band-notch { position: absolute; left: 535px; top: 446px; width: 0; height: 0;
    border-left: 8px solid transparent; border-right: 8px solid transparent; border-top: 14px solid var(--hero-bg); }
  .contact-icon { position: absolute; top: 493px; width: 52px; height: 52px; }
  .contact-text { position: absolute; font-size: 9px; line-height: 16px; color: var(--white); font-weight: 600; }

  .section-head { position: absolute; left: 175px; top: 632px; width: 739px; height: 34px;
    display: flex; align-items: center; gap: 12px; }
  .section-rule { flex: 1; height: 1px; background: #dbe9d9; }
  .section-title { flex: none; font-family: "Josefin Sans", Arial, sans-serif; font-weight: 300; font-size: 27px;
    letter-spacing: 0.5px; line-height: 34px; padding-top: 4px; color: var(--green-text); }
  .column { position: absolute; top: 698px; width: 332px; font-size: 10.6px; line-height: 13.4px; color: var(--ink); }
  .column p { margin-bottom: 13.4px; }

  .footer { position: absolute; left: 0; top: 1084px; width: 1086px; height: 116px;
    background: linear-gradient(90deg, #36b13f, #3bbd44 50%, #33ac3c); border-top: 4px solid #45c84d; }
  .footer-base { position: absolute; left: 0; bottom: 0; width: 100%; height: 11px; background: var(--green-deep); }
  .footer-col { position: absolute; top: 24px; color: var(--white); font-size: 9px; line-height: 14px; }
  .footer-col h3 { font-size: 10.5px; font-weight: 600; letter-spacing: 0.4px; color: #2b6b2e; margin-bottom: 13px; display: flex; align-items: center; gap: 6px; }
  .footer-col h3 svg { flex: none; }
  .footer-col .links { padding-left: 16px; }
  .footer-mark { position: absolute; left: 660px; top: 37px; font-weight: 600; font-size: 18px; color: var(--white); }
  .footer-copy { position: absolute; left: 765px; top: 34px; font-size: 9px; line-height: 12px; font-weight: 600; color: var(--white); }
</style>
</head>
<body>

<header class="hero">
  <div class="hero-photo" role="img" aria-label="Foto: Läuferin mit rotem Haar auf einer baumgesäumten Laufbahn"></div>

  <div class="brand">
    <div class="brand-name">wolterhagen</div>
    <div class="brand-tag">Physiotherapeut</div>
  </div>

  <div class="nav-marker"></div>
  <nav class="nav">
    <a class="active" style="left:509px">HOME</a>
    <a style="left:583px">SHOP</a>
    <a style="left:654px">COOPERATION</a>
    <a style="left:750px">CONTACT US</a>
  </nav>
  <span class="social one" aria-label="Soziales Netzwerk"></span>
  <span class="social two" aria-label="Soziales Netzwerk"></span>

  <div class="hero-divider" style="left:333px;width:143px"></div>
  <div class="hero-divider" style="left:608px;width:144px"></div>
  <div class="hero-dot"></div>

  <h1 class="hero-title">“LOREM IPSUM DOLOR AMET”</h1>
  <p class="hero-copy" style="top:274px">Lorem ipsum ad his scripta blandit partiendo eum fastidii accumsan euripidis in, eum liber hendrerit an</p>
  <p class="hero-copy" style="top:308px">ut wisisuscipiantur, quo dicit ridens inciderint iduo mundi lobortis refor midans eu, legimus senserit definie an eos, eu sit tincidunt incorru definitionem, vis mutat affert percipit.</p>
</header>

<section class="contact-band">
  <div class="band-photo" role="img" aria-label="Foto: Radsportler mit Helm, grün eingefärbt, rechts Stadtplan im Hintergrund"></div>
</section>
<div class="band-notch"></div>

<svg class="contact-icon" style="left:248px" viewBox="0 0 52 52" aria-hidden="true">
  <circle cx="26" cy="26" r="24.5" fill="none" stroke="#fff" stroke-width="2"/>
  <path d="M26 13c-6 0-10 4.5-10 10 0 7 10 17 10 17s10-10 10-17c0-5.5-4-10-10-10z" fill="#fff"/>
  <circle cx="26" cy="23" r="4" fill="#3dbf46"/>
</svg>
<div class="contact-text" style="left:326px;top:506px">Lindenweg S #482,<br>City Country</div>

<svg class="contact-icon" style="left:487px" viewBox="0 0 52 52" aria-hidden="true">
  <circle cx="26" cy="26" r="24.5" fill="none" stroke="#fff" stroke-width="2"/>
  <path d="M29 15l3 5-3 3c1 3 2 5 0 8l-3 2-2 3c5 1 9-3 11-8 2-4 1-9-3-13z" fill="#fff" transform="rotate(15 26 26)"/>
</svg>
<div class="contact-text" style="left:563px;top:512px">+561-40718823</div>

<svg class="contact-icon" style="left:689px" viewBox="0 0 52 52" aria-hidden="true">
  <circle cx="26" cy="26" r="24.5" fill="none" stroke="#fff" stroke-width="2"/>
  <rect x="14" y="16" width="24" height="19" rx="2" fill="#fff"/>
  <rect x="16" y="19" width="20" height="3" fill="#3dbf46"/>
  <rect x="16" y="24" width="20" height="1.4" fill="#3dbf46"/>
  <rect x="16" y="27" width="20" height="1.4" fill="#3dbf46"/>
  <rect x="16" y="30" width="20" height="1.4" fill="#3dbf46"/>
</svg>
<div class="contact-text" style="left:764px;top:508px;font-weight:400">email@wolterhagen.com</div>

<div class="section-head">
  <span class="section-rule"></span>
  <h2 class="section-title">LOREM SIT</h2>
  <span class="section-rule"></span>
</div>

<main>
  <div class="column" style="left:196px">
    <p>Lorem ipsum ad his scripta blandit partiendo eum fastidii accumsan euripidis in, eum liber hendrerit an ut wisisuscipiantur, quo dicit ridens inciderint id. Quo mundi lobortis refor midans eu, legimus senserit definie an eos, eu sit tincidunt incorru definitionem, vis mutat affert percipit.</p>
    <p>Ad his scripta blandit partiendo eum fastidii accumsan euripidis in, eum liber hendrerit an ut wisisuscipiantur, quo dicit ridens inciderint id. Quo mundi lobortis refor midans eu, legimus senserit definie an eos, eu sit tincidunt incorru definitionem, vis mutat affert percipit ipsum ad his scripta blandit partiendo eum fastidii accumsan euripidis in, eum liber hendrerit an ut wisisuscipiantur, quo dicit ridens inciderint id. Quo mundi lobortis refor midans eu, legimus senserit definie an eos, eu sit tincidunt incorru definitionem, vis mutat affert percipit.</p>
    <p>Lorem ipsum ad his scripta blandit partiendo eum fastidii accumsan euripidis in, eum liber hendrerit an ut wisisuscipiantur, quo dicit ridens inciderint id. Quo mundi lobortis refor midans eu, legimus senserit definie an eos, eu sit tincidunt incorru definitionem, vis mutat affert percipit.</p>
    <p>Scripta blandit partiendo eum fastidii accumsan euripidis in, eum liber hendrerit an ut wisisuscipiantur, quo dicit ridens inciderint id. Quo mundi lobortis refor midans eu, legimus senserit definie an eos, eu sit tincidunt incorru definitionem, vis mutat affert percipit.</p>
  </div>
  <div class="column" style="left:569px">
    <p>Lorem ipsum ad his scripta blandit partiendo eum fastidii accumsan euripidis in, eum liber hendrerit an ut wisisuscipiantur, quo dicit ridens inciderint id. Quo mundi lobortis refor midans eu, legimus senserit definie an eos, eu sit tincidunt incorru definitionem, vis mutat affert percipit.</p>
    <p>Ad his scripta blandit partiendo eum fastidii accumsan euripidis in, eum liber hendrerit an ut wisisuscipiantur, quo dicit ridens inciderint id. Quo mundi lobortis refor midans eu, legimus senserit definie an eos, eu sit tincidunt incorru definitionem, vis mutat affert percipit ipsum ad his scripta blandit partiendo eum fastidii accumsan euripidis in, eum liber hendrerit an ut wisisuscipiantur, quo dicit ridens inciderint id. Quo mundi lobortis refor midans eu, legimus senserit definie an eos, eu sit tincidunt incorru definitionem, vis mutat affert percipit.</p>
    <p>Lorem ipsum ad his scripta blandit partiendo eum fastidii accumsan euripidis in, eum liber hendrerit an ut wisisuscipiantur, quo dicit ridens inciderint id. Quo mundi lobortis refor midans eu, legimus senserit definie an eos, eu sit tincidunt incorru definitionem, vis mutat affert percipit.</p>
    <p>Scripta blandit partiendo eum fastidii accumsan euripidis in, eum liber hendrerit an ut wisisuscipiantur, quo dicit ridens inciderint id. Quo mundi lobortis refor midans eu, legimus senserit definie an eos, eu sit tincidunt incorru definitionem, vis mutat affert percipit.</p>
  </div>
</main>

<footer class="footer">
  <div class="footer-col" style="left:199px">
    <h3><svg width="10" height="12" viewBox="0 0 10 12"><path d="M5 0C2.2 0 0 2.1 0 4.8 0 8 5 12 5 12s5-4 5-7.2C10 2.1 7.8 0 5 0z" fill="#2b6b2e"/><circle cx="5" cy="4.8" r="1.8" fill="#3bbd44"/></svg>CONTACT US :</h3>
    <div class="links">email@wolterhagen.com<br>Phone: 866-430-5172</div>
  </div>
  <div class="footer-col" style="left:363px">
    <h3><svg width="15" height="11" viewBox="0 0 15 11"><rect width="15" height="11" rx="1" fill="#2b6b2e"/><rect x="2" y="3" width="11" height="1.2" fill="#3bbd44"/><rect x="2" y="6" width="11" height="1.2" fill="#3bbd44"/></svg>ABOUT US :</h3>
    <div class="links" style="margin-top:-2px">About Us</div>
  </div>
  <div class="footer-col" style="left:510px">
    <h3><svg width="11" height="12" viewBox="0 0 11 12"><circle cx="5.5" cy="3" r="3" fill="#2b6b2e"/><path d="M0 12c0-4 2.5-6 5.5-6S11 8 11 12z" fill="#2b6b2e"/></svg>SERVICE :</h3>
    <div class="links">Shop<br>Cooperation</div>
  </div>
  <div class="footer-mark">wolterhagen</div>
  <div class="footer-copy">Copyright wolterhagen<br>2015. All rights reserved.</div>
  <div class="footer-base"></div>
</footer>

</body>
</html>
```